integrative health clinic-Medical massage, acupuncture, chiropractic

we like our logo, but are open to new ideas. We need a new card design. We have added chiropractic and acupuncture that we have put under the name of the business. We are an integrative medical clinic

Target Market(s)

General public, athletes

Contact Information for Business Card

Phone 5055583927
Fax 5055583926
Hours Monday-Friday 9-6
Saturday 10-6
The 20% can be smaller on the back

Colors
3176b5
0355a3

Requirements
Must have
• Logo but am open to ideas
Nice to have
• We are an integrated medical clinic but also want to be personable. We want the card fun and inviting

```html
<!DOCTYPE html>
<html lang="en">
<head>
<meta charset="utf-8">
<title>Vital Core Wellness – Business Card</title>
<link href="https://fonts.googleapis.com/css2?family=Crimson+Text:ital@1&family=Lato:wght@400;700&display=swap" rel="stylesheet">
<style>
  :root {
    --brand-blue: #3176b5;
    --brand-deep: #0355a3;
    --brand-light: #4a8fcb;
    --paper: #ffffff;
    --ink: #1c1c2a;
    --backdrop: #3a3a3a;
  }
  html, body {
    margin: 0;
    width: 1200px;
    height: 1195px;
    overflow: hidden;
    background: var(--backdrop);
    font-family: "Lato", sans-serif;
  }
  .card {
    position: absolute;
    left: 150px;
    width: 900px;
    height: 514px;
    border-radius: 34px;
    overflow: hidden;
    box-shadow: 0 14px 30px rgba(0,0,0,.45);
  }
  .card-back { top: 50px; }
  .card-front { top: 630px; background: var(--paper); }
  .card svg.bands { position: absolute; inset: 0; }

  .brand-block { position: absolute; right: 56px; text-align: right; }
  .brand { display: flex; align-items: center; justify-content: flex-end; gap: 12px; }
  .brand-dot { width: 26px; height: 26px; border-radius: 50%; }
  .brand-name { font-weight: 700; font-size: 40px; letter-spacing: -0.5px; line-height: 1.1; }
  .brand-tag {
    margin-top: 4px;
    font-family: "Crimson Text", serif;
    font-style: italic;
    font-size: 20px;
    letter-spacing: .3px;
  }

  /* back side */
  .card-back .brand-block { top: 46px; }
  .card-back .brand-dot { background: var(--paper); }
  .card-back .brand-name, .card-back .brand-tag { color: var(--paper); }
  .offer {
    position: absolute; left: 60px; top: 208px;
    color: var(--paper); font-weight: 700; font-size: 22px; letter-spacing: 6px;
  }
  .hours { position: absolute; left: 60px; top: 262px; color: var(--paper); font-weight: 700; line-height: 1.15; }
  .hours .label { font-size: 22px; }
  .hours .line { font-size: 17px; }
  .insurance { position: absolute; left: 60px; top: 350px; color: var(--paper); font-weight: 700; font-size: 21px; line-height: 1.2; }
  .booking { position: absolute; right: 56px; bottom: 44px; text-align: right; color: var(--paper); font-weight: 700; }
  .booking .cta { font-size: 25px; }
  .booking .url { font-size: 19px; font-weight: 400; }

  /* front side */
  .card-front .brand-block { top: 80px; }
  .card-front .brand-dot { background: var(--brand-deep); }
  .card-front .brand-name, .card-front .brand-tag { color: var(--ink); }
  .specialty { position: absolute; left: 68px; top: 128px; color: var(--brand-blue); font-weight: 700; font-size: 23px; line-height: 1.15; }
  .address { position: absolute; left: 68px; top: 222px; color: var(--brand-deep); font-weight: 700; font-size: 23px; line-height: 1.1; }
  .contacts { position: absolute; left: 68px; top: 298px; margin: 0; padding: 0; list-style: none; color: var(--brand-blue); font-size: 23px; }
  .contacts li { display: flex; align-items: center; gap: 10px; height: 30px; }
  .contacts svg { width: 22px; height: 22px; flex: none; }
</style>
</head>
<body>

<section class="card card-back">
  <svg class="bands" viewBox="0 0 900 514" preserveAspectRatio="none" aria-hidden="true">
    <defs>
      <linearGradient id="backGlow" x1="0" y1="0" x2="1" y2="0.4">
        <stop offset="0" stop-color="#3176b5"/>
        <stop offset="0.7" stop-color="#4a8fcb"/>
        <stop offset="1" stop-color="#3a80c0"/>
      </linearGradient>
    </defs>
    <rect width="900" height="514" fill="url(#backGlow)"/>
    <path d="M0 514 C 420 470 760 360 900 120 L900 514 Z" fill="#ffffff"/>
    <path d="M0 514 C 440 490 790 380 900 150 L900 514 Z" fill="#0355a3"/>
  </svg>
  <div class="brand-block">
    <div class="brand"><span class="brand-dot"></span><span class="brand-name">Vital Core Wellness</span></div>
    <div class="brand-tag">Medical Massage, Acupuncture and Chiropractic</div>
  </div>
  <div class="offer">20% OFF FIRST VISIT</div>
  <div class="hours">
    <div class="label">Hours</div>
    <div class="line">Monday-Friday 9-6</div>
    <div class="line">Saturday 10-6</div>
  </div>
  <div class="insurance">We accept some insurance<br>workers Comp and Personal Injury</div>
  <div class="booking">
    <div class="cta">Book Online</div>
    <div class="url">www.vitalcorewellnessnm.com</div>
  </div>
</section>

<section class="card card-front">
  <svg class="bands" viewBox="0 0 900 514" preserveAspectRatio="none" aria-hidden="true">
    <path d="M0 0 L560 0 C 300 10 120 40 0 110 Z" fill="#3176b5"/>
    <path d="M0 0 L520 0 C 280 8 110 35 0 95 Z" fill="#0355a3"/>
    <path d="M900 300 C 760 420 560 480 300 514 L900 514 Z" fill="#3176b5"/>
    <path d="M900 318 C 770 440 580 495 360 514 L900 514 Z" fill="#0355a3"/>
  </svg>
  <div class="brand-block">
    <div class="brand"><span class="brand-dot"></span><span class="brand-name">Vital Core Wellness</span></div>
    <div class="brand-tag">Medical Massage, Acupuncture and Chiropractic</div>
  </div>
  <div class="specialty">Specializing in Medical<br>Sports massage<br>and Manual Therapies</div>
  <div class="address">1437 Cerrillos Way h2<br>Santa Fe, NM 87505</div>
  <ul class="contacts">
    <li>
      <svg viewBox="0 0 24 24" aria-label="Phone"><circle cx="12" cy="12" r="11" fill="none" stroke="#3176b5" stroke-width="2"/><path d="M7 10c0-2 10-2 10 0l-1 1h-2l-1-1h-2l-1 1H8z M8 13h8v4H8z" fill="#3176b5"/></svg>
      5055583927
    </li>
    <li>
      <svg viewBox="0 0 24 24" aria-label="Fax"><circle cx="12" cy="12" r="11" fill="none" stroke="#3176b5" stroke-width="2"/><rect x="8" y="6" width="8" height="4" fill="none" stroke="#3176b5" stroke-width="1.6"/><rect x="6" y="10" width="12" height="5" fill="#3176b5"/><rect x="8" y="15" width="8" height="3" fill="none" stroke="#3176b5" stroke-width="1.6"/></svg>
      5055583926
    </li>
    <li>
      <svg viewBox="0 0 24 24" aria-label="Email"><circle cx="12" cy="12" r="11" fill="none" stroke="#3176b5" stroke-width="2"/><rect x="6" y="8" width="12" height="8" fill="#3176b5"/><path d="M6 8l6 5 6-5" fill="none" stroke="#fff" stroke-width="1.4"/></svg>
      Info@vitalcorewellnessnm.com
    </li>
    <li>
      <svg viewBox="0 0 24 24" aria-label="Website"><circle cx="12" cy="12" r="11" fill="none" stroke="#3176b5" stroke-width="2"/><circle cx="12" cy="12" r="7" fill="none" stroke="#3176b5" stroke-width="1.4"/><ellipse cx="12" cy="12" rx="3" ry="7" fill="none" stroke="#3176b5" stroke-width="1.4"/><path d="M5 12h14" stroke="#3176b5" stroke-width="1.4"/></svg>
      www.vitalcorewellnessnm.com
    </li>
  </ul>
</section>

</body>
</html>
```